Portal Panel Medic need professional looking business card printed on plastic, Commericial, Industri

We are family owned and operated garage door company in Indianapolis, Indiana. We sale service and install dock equipment, doors, operators. We are looking to expand our commercial/ industrial division. We also service all residential doors and operators. We are looking for a business that stands out of the crowd. We are committed to have the best customer service in the industry.

Target Market(s)

National and local general contractors, National/ Corpate service accounts,

Industry/Entity Type

Business Service

Contact Information for Business Card

To be printed on plastic stock

Font styles to use
Sans Serif

Colors
ffffff
f04a50
ec1f27

Requirements
Must have
• Name, website,email, phone number, position.
Nice to have
• A standout professional design

```html
<!DOCTYPE html>
<html lang="en">
<head>
<meta charset="utf-8">
<title>Portal Panel Medic – Business Card</title>
<link rel="stylesheet" href="https://fonts.googleapis.com/css2?family=Roboto+Condensed:wght@700&family=Roboto:wght@400&display=swap">
<style>
  :root {
    --page-bg: #e4e4e4;
    --card-light: #e2dfd8;
    --card-mid: #d3d0c8;
    --card-dark: #bdbab3;
    --brand-red: #ec1f27;
    --deep-red: #c3161d;
    --ink: #141414;
    --text: #2a2a2a;
  }
  * { margin: 0; padding: 0; box-sizing: border-box; }
  html, body {
    width: 1200px; height: 900px; overflow: hidden;
    background: var(--page-bg);
  }
  .card {
    position: absolute;
    left: 120px; top: 176px;
    width: 960px; height: 548px;
    border-radius: 30px;
    background: linear-gradient(115deg, var(--card-light) 0%, var(--card-mid) 60%, var(--card-dark) 100%);
    box-shadow: 0 8px 24px rgba(0,0,0,0.18);
  }
  .brand {
    position: absolute;
    left: 100px; top: 168px;
    display: flex; align-items: center; gap: 18px;
  }
  .brand-figure {
    width: 110px; height: 220px;
    border-radius: 10px;
    background: linear-gradient(180deg, #cfc9c1 0%, #8d7e72 55%, #5b3a2c 100%);
  }
  .brand-name {
    font-family: "Roboto", Arial, sans-serif;
    font-weight: 400;
    font-size: 34px;
    line-height: 1.2;
    white-space: nowrap;
    color: var(--brand-red);
  }
  .contact {
    position: absolute;
    left: 560px; top: 150px;
  }
  .person-name {
    font-family: "Roboto Condensed", "Arial Narrow", sans-serif;
    font-weight: 700;
    font-size: 40px;
    color: var(--ink);
    letter-spacing: -0.5px;
  }
  .person-role {
    font-family: "Roboto", Arial, sans-serif;
    font-size: 19px;
    color: var(--deep-red);
    margin-top: 2px;
  }
  .contact-list {
    list-style: none;
    margin-top: 38px;
    font-family: "Roboto", Arial, sans-serif;
    font-size: 21px;
    color: var(--text);
  }
  .contact-list li {
    display: flex; align-items: center; gap: 16px;
    height: 36px;
  }
  .contact-list svg { width: 20px; height: 20px; fill: var(--deep-red); flex: none; }
  .web-domain { color: var(--deep-red); }
</style>
</head>
<body>
  <div class="card">
    <div class="brand">
      <div class="brand-figure" role="img" aria-label="Mascot illustration area: cartoon door technician"></div>
      <div class="brand-name">Portal Panel Medic</div>
    </div>

    <div class="contact">
      <div class="person-name">John Doe Smith</div>
      <div class="person-role">Managing Director</div>
      <ul class="contact-list">
        <li>
          <svg viewBox="0 0 24 24" aria-hidden="true"><path d="M4 9c0-3 4-5 8-5s8 2 8 5v2h-4V9.5c-1-.6-2.5-1-4-1s-3 .4-4 1V11H4zM7 12h10l2 7H5z"/><circle cx="12" cy="15.5" r="1.8" fill="#d3d0c8"/></svg>
          <span>(317) 555-0142</span>
        </li>
        <li>
          <svg viewBox="0 0 24 24" aria-hidden="true"><path d="M2 5h20v14H2z"/><path d="M2 5l10 8 10-8" fill="none" stroke="#d3d0c8" stroke-width="1.8"/></svg>
          <span>john@portalpanelmedicllc.com</span>
        </li>
        <li>
          <svg viewBox="0 0 24 24" aria-hidden="true"><circle cx="12" cy="12" r="10"/><path d="M2 12h20M12 2c3 3 3 17 0 20M12 2c-3 3-3 17 0 20M4 7h16M4 17h16" fill="none" stroke="#d3d0c8" stroke-width="1.3"/></svg>
          <span>www.<span class="web-domain">portalpanelmedicllc.com</span></span>
        </li>
      </ul>
    </div>
  </div>
</body>
</html>
```